Solace Chiropractic & Acupuncture Business Cards

I need a business card design that feels elevated. I am open to any of the logo designs uploaded. We have two doctors so I'll need to be able to change out the names.

Information:
Marnie Toller D.C., Dipl. Ac. ASA
584 W 12th St, Ste 320
Wrenfield, CO 67419
solacegrove.net
620-555-0147
drmarnie@solacegrove.com
Updates

We have designs we like now, we are just trying to choose between top contenders. Thanks for your submissions!

Contact Information for Business Card

noted in description

Requirements
Must have
• ability to edit info if possible
Nice to have
• Please see our website solacegrove.net for our style and colors

```html
<!DOCTYPE html>
<html lang="en">
<head>
<meta charset="utf-8">
<title>Solace Chiropractic &amp; Acupuncture — Business Cards</title>
<link rel="stylesheet" href="https://fonts.googleapis.com/css2?family=Tinos:wght@400&display=swap">
<style>
  :root {
    --page-bg: #d9d8d4;
    --card-bg: #efeee8;
    --ink: #2b3246;
    --rule: #6f7382;
    --shadow: rgba(20, 22, 30, 0.18);
  }
  * { box-sizing: border-box; margin: 0; padding: 0; }
  html, body {
    width: 1200px;
    height: 900px;
    overflow: hidden;
    background: var(--page-bg);
    font-family: "Tinos", "Times New Roman", serif;
    color: var(--ink);
  }
  .sheet {
    position: relative;
    width: 1200px;
    height: 900px;
  }
  .card {
    position: absolute;
    width: 665px;
    height: 380px;
    background: var(--card-bg);
    box-shadow: 0 6px 18px var(--shadow);
  }
  .card--front { left: 268px; top: 48px; }
  .card--back  { left: 268px; top: 472px; }

  .wordmark {
    display: flex;
    flex-direction: column;
    align-items: flex-end;
    font-weight: 400;
    color: var(--ink);
  }
  .wordmark__name { line-height: 1; letter-spacing: -0.01em; }
  .wordmark__tagline { text-transform: uppercase; letter-spacing: 0.04em; }

  .card--front .wordmark {
    position: absolute;
    left: 50%;
    top: 50%;
    transform: translate(-50%, -50%);
  }
  .card--front .wordmark__name { font-size: 92px; }
  .card--front .wordmark__tagline { font-size: 13px; margin-top: 4px; }

  .card--back .wordmark {
    position: absolute;
    right: 44px;
    top: 52px;
  }
  .card--back .wordmark__name { font-size: 58px; }
  .card--back .wordmark__tagline { font-size: 8.5px; margin-top: 2px; }

  .person {
    position: absolute;
    left: 46px;
    top: 52px;
  }
  .person__name { font-size: 30px; line-height: 1.1; font-weight: 400; }
  .person__credentials { font-size: 12px; margin-top: 4px; }

  .divider {
    position: absolute;
    left: 32px;
    right: 32px;
    top: 150px;
    height: 1px;
    background: var(--rule);
  }

  .address {
    position: absolute;
    left: 46px;
    top: 178px;
    font-size: 16px;
    line-height: 1.45;
    font-style: normal;
  }

  .contact {
    position: absolute;
    left: 360px;
    top: 236px;
    font-size: 17px;
    line-height: 1.5;
    list-style: none;
  }
  .contact__label { display: inline-block; width: 26px; }
</style>
</head>
<body>
<main class="sheet">

  <section class="card card--front" aria-label="Card front">
    <div class="wordmark">
      <span class="wordmark__name">Solace</span>
      <span class="wordmark__tagline">Chiropractic &amp; Acupuncture</span>
    </div>
  </section>

  <section class="card card--back" aria-label="Card back">
    <div class="person">
      <h1 class="person__name">Marnie Toller</h1>
      <p class="person__credentials">D.C., Dipl. Ac. ASA</p>
    </div>

    <div class="wordmark">
      <span class="wordmark__name">Solace</span>
      <span class="wordmark__tagline">Chiropractic &amp; Acupuncture</span>
    </div>

    <div class="divider"></div>

    <address class="address">
      Solace Chiropractic &amp; Acupuncture<br>
      584 W 12th St,<br>
      Ste 320, Wrenfield, CO 67419
    </address>

    <ul class="contact">
      <li><span class="contact__label">M.</span>(620) 555-0183</li>
      <li><span class="contact__label">W.</span>www.solacegrove.net</li>
      <li><span class="contact__label">E.</span>drmarnie@solacegrove.com</li>
    </ul>
  </section>

</main>
</body>
</html>
```